Business Card Design needed - Something Awesome!

Need a business card designed. Company is "Harbor Vane Consulting" we do consulting and also have sales automation technology.
I'm going to use thick stock or metal, something really nice... I was thinking about a QR Code on the back that would just upload my contact info to the persons contact, etc -

This is a Strategy Company with a tech feel. I'm open to ideas but really want this to be nice!

I need a template that should include:

Name | Position or Title
D: 555.203.8146
www.harborvaneconsulting.example

I'm going to attach my contact so you can use that one, I need to get this printed.

Target Market(s)

Small to mid size customers, Entrepreneurs etc.

Industry/Entity Type

Consulting, Tech, Private Equity.

Contact Information for Business Card

Name, Phone, Maybe email, URL

Font styles to use
Sans Serif

Colors

Designer to choose only greyscale colors for use in the design.

Requirements
Must have
• Fresh, Clean, stand out from the crowd - will be on thick stock or metal.
Nice to have
• Clean, simple yet impactful.
Should not have
• Not cartoonish

```html
<!DOCTYPE html>
<html lang="en">
<head>
<meta charset="UTF-8">
<title>Harbor Vane Consulting — Business Card</title>
<link href="https://fonts.googleapis.com/css2?family=Lato:wght@300;400;700&display=swap" rel="stylesheet">
<style>
  :root {
    --backdrop: #1e1e1e;
    --card-dark: #232323;
    --card-light: #e3e5e4;
    --ink-dark: #1a1a1a;
    --ink-mid: #3a3a3a;
    --wordmark: #9a9a9a;
    --edge: #3a3a3a;
  }
  * { margin: 0; padding: 0; box-sizing: border-box; }
  html, body {
    width: 1200px;
    height: 958px;
    overflow: hidden;
    background: var(--backdrop);
    font-family: "Lato", sans-serif;
  }
  .sheet {
    width: 1200px;
    height: 958px;
    display: flex;
    flex-direction: column;
    align-items: center;
    justify-content: center;
    gap: 58px;
  }
  .card {
    width: 700px;
    height: 400px;
    border-radius: 4px;
    position: relative;
    box-shadow: 0 0 0 1px var(--edge);
  }
  .card--front {
    background: var(--card-dark);
    display: flex;
    align-items: center;
    justify-content: center;
  }
  .wordmark {
    display: flex;
    align-items: center;
    gap: 22px;
  }
  .wordmark__square {
    width: 30px;
    height: 30px;
    background: var(--wordmark);
  }
  .wordmark__name {
    font-weight: 300;
    font-size: 68px;
    letter-spacing: 4px;
    text-transform: uppercase;
    color: var(--wordmark);
  }
  .card--back {
    background: var(--card-light);
  }
  .back__brand {
    position: absolute;
    top: 44px;
    right: 52px;
    font-weight: 700;
    font-size: 17px;
    letter-spacing: 2px;
    text-transform: uppercase;
    color: var(--ink-dark);
  }
  .contact {
    position: absolute;
    right: 52px;
    bottom: 52px;
    text-align: right;
    color: var(--ink-dark);
  }
  .contact__name {
    font-weight: 700;
    font-size: 30px;
    line-height: 1.1;
  }
  .contact__title {
    font-weight: 400;
    font-size: 18px;
    color: var(--ink-mid);
    margin-top: 4px;
  }
  .contact__rule {
    width: 24px;
    height: 2px;
    background: var(--ink-dark);
    margin: 14px 0 14px auto;
  }
  .contact__line {
    font-size: 15px;
    line-height: 1.5;
    color: var(--ink-mid);
  }
</style>
</head>
<body>
  <main class="sheet">
    <section class="card card--front" aria-label="Card front">
      <div class="wordmark">
        <span class="wordmark__square"></span>
        <span class="wordmark__name">Harbor Vane</span>
      </div>
    </section>

    <section class="card card--back" aria-label="Card back">
      <div class="back__brand">Harbor Vane</div>
      <div class="contact">
        <div class="contact__name">Dorian K. Hale</div>
        <div class="contact__title">Founder/CEO</div>
        <div class="contact__rule"></div>
        <div class="contact__line">555.203.8146</div>
        <div class="contact__line">hello@harborvaneconsulting.example</div>
        <div class="contact__line">www.harborvaneconsulting.example</div>
      </div>
    </section>
  </main>
</body>
</html>
```